Professional & attention grabbing.

A business card design, front and back. I already have a logo I will attach, but I am open to something new as well.
Things to include:
Name:
Title:
Phone:
Email:
Wanting something that is professional but attention grabbing.
Also we do a lot of work using drones on natural gas pipelines (leading the future)if you want to include any of that. I'm open to ideas.
Target Market(s)
Natural gas transmission industry / greenhouse gas mitigation industry
Industry/Entity Type
Business
Contact Information for Business Card
All details have been conveyed above.
Colors
Designer to choose colors to be used in the design.
Look and feel
Each slider illustrates characteristics of the customer's brand and the style your logo design should communicate.

```html
<!DOCTYPE html>
<html lang="en">
<head>
<meta charset="utf-8">
<title>KV Field Inspections – Business Card</title>
<link rel="stylesheet" href="https://fonts.googleapis.com/css2?family=Michroma&family=Roboto:wght@500;700&display=swap">
<style>
  :root {
    --board: #a8a9ac;
    --label: #111111;
    --ink: #3a3a3c;
    --white: #ffffff;
    --gold-light: #f4d35e;
    --gold: #f0bf3a;
    --amber: #e8a030;
    --orange: #e08a2a;
    --red: #c9202a;
  }
  html, body {
    margin: 0;
    padding: 0;
    overflow: hidden;
  }
  .presentation {
    position: relative;
    width: 1200px;
    height: 1200px;
    background: var(--board);
    overflow: hidden;
  }
  .side-label {
    position: absolute;
    left: 80px;
    margin: 0;
    font-family: "Michroma", sans-serif;
    font-size: 24px;
    letter-spacing: 4px;
    color: var(--label);
    line-height: 1;
  }
  .side-label--front { top: 280px; }
  .side-label--back { top: 802px; }
  .card {
    position: absolute;
    left: 277.5px;
    width: 675px;
    height: 412.5px;
    display: block;
    box-shadow: 0 18px 26px rgba(0,0,0,0.18);
  }
  .card--front { top: 108px; }
  .card--back { top: 618px; }
  .brand-name {
    font-family: "Roboto", sans-serif;
    font-weight: 700;
    fill: var(--ink);
  }
  .holder-name, .holder-title, .contact-text {
    font-family: "Roboto", sans-serif;
    font-weight: 700;
    fill: var(--ink);
  }
  .contact-text { font-weight: 500; }
</style>
</head>
<body>
<main class="presentation">
  <p class="side-label side-label--front">FRONT</p>
  <p class="side-label side-label--back">BACK</p>

  <!-- Front of card -->
  <svg class="card card--front" viewBox="0 0 450 275" xmlns="http://www.w3.org/2000/svg" aria-label="Card front">
    <defs>
      <linearGradient id="wedgeLeft" x1="0" x2="1" y1="0" y2="0">
        <stop offset="0" stop-color="var(--gold)"/>
        <stop offset="1" stop-color="var(--orange)"/>
      </linearGradient>
      <linearGradient id="wedgeRight" x1="0" x2="1" y1="0" y2="0">
        <stop offset="0" stop-color="var(--gold-light)"/>
        <stop offset="1" stop-color="var(--orange)"/>
      </linearGradient>
      <filter id="foldShadow" x="-20%" y="-20%" width="140%" height="140%">
        <feDropShadow dx="2" dy="0" stdDeviation="3" flood-color="#000" flood-opacity="0.35"/>
      </filter>
    </defs>
    <rect class="card-ground" width="450" height="275" fill="var(--white)"/>

    <g class="chevron chevron--left">
      <polygon points="0,0 25,0 160,137 25,275 0,275" fill="url(#wedgeLeft)"/>
      <polygon points="0,18 118,137 0,257" fill="url(#wedgeLeft)" filter="url(#foldShadow)"/>
      <polygon points="0,40 97,137 0,235" fill="var(--gold)" opacity="0.55"/>
    </g>

    <g class="chevron chevron--right">
      <polygon points="450,0 425,0 293,137 425,275 450,275" fill="url(#wedgeRight)"/>
      <polygon points="450,18 332,137 450,257" fill="url(#wedgeRight)" filter="url(#foldShadow)"/>
      <polygon points="450,40 353,137 450,235" fill="var(--orange)" opacity="0.5"/>
    </g>

    <g class="brand">
      <rect x="163" y="130" width="11" height="11" fill="var(--red)"/>
      <text class="brand-name" x="178" y="140" font-size="11.5">KV Field Inspections</text>
    </g>
  </svg>

  <!-- Back of card -->
  <svg class="card card--back" viewBox="0 0 450 275" xmlns="http://www.w3.org/2000/svg" aria-label="Card back">
    <defs>
      <linearGradient id="backGround" x1="0" x2="1" y1="0" y2="0">
        <stop offset="0" stop-color="var(--gold-light)"/>
        <stop offset="0.3" stop-color="var(--gold)"/>
        <stop offset="0.65" stop-color="var(--amber)"/>
        <stop offset="1" stop-color="var(--orange)"/>
      </linearGradient>
      <linearGradient id="midBar" x1="0" x2="1" y1="0" y2="0">
        <stop offset="0" stop-color="var(--gold-light)"/>
        <stop offset="1" stop-color="var(--amber)"/>
      </linearGradient>
      <filter id="edgeShadow" x="-20%" y="-20%" width="140%" height="140%">
        <feDropShadow dx="0" dy="1.5" stdDeviation="2" flood-color="#000" flood-opacity="0.4"/>
      </filter>
    </defs>
    <rect class="card-ground" width="450" height="275" fill="url(#backGround)"/>

    <g class="fold-lines" fill="none" stroke="rgba(90,50,0,0.35)" stroke-width="1.5" filter="url(#edgeShadow)">
      <polyline points="0,22 114,136 0,250"/>
      <polyline points="0,48 90,137 0,226"/>
      <polyline points="450,22 336,136 450,250"/>
      <polyline points="450,48 360,137 450,226"/>
    </g>

    <rect class="center-bar" x="47" y="134" width="356" height="7" fill="url(#midBar)" opacity="0.8"/>
    <rect x="396" y="129" width="4" height="15" rx="1.5" fill="var(--gold-light)"/>
    <rect x="278" y="127" width="6" height="3" rx="1" fill="var(--gold-light)"/>

    <polygon class="accent accent--left" points="0,85 47,138 0,192" fill="var(--red)"/>
    <polygon class="accent accent--right" points="450,85 403,138 450,192" fill="var(--red)"/>

    <text class="holder-name" x="225" y="89" font-size="21" text-anchor="middle">Name</text>
    <text class="holder-title" x="223" y="112" font-size="15" text-anchor="middle">Title</text>

    <g class="contact contact--phone">
      <rect x="173" y="174" width="7" height="12" rx="1.5" fill="none" stroke="var(--ink)" stroke-width="1"/>
      <line x1="175.5" y1="184" x2="177.5" y2="184" stroke="var(--ink)" stroke-width="0.8"/>
      <text class="contact-text" x="193" y="184" font-size="8">+63 900 555 0142</text>
    </g>
    <g class="contact contact--email">
      <circle cx="176.5" cy="201.5" r="4.5" fill="none" stroke="var(--ink)" stroke-width="1"/>
      <circle cx="176.5" cy="201.5" r="1.8" fill="none" stroke="var(--ink)" stroke-width="0.9"/>
      <text class="contact-text" x="193" y="205" font-size="8">info@kvfield.com</text>
    </g>
  </svg>
</main>
</body>
</html>
```